Bright Arrow Delivery Service Wordpress design

My client is a delivery service whose motto is "We go where the freight leads us." Their colors are red, white and blue. They use Voyalo vans and box vans - NO semi tractors. They like this Website design www.tovamu-sample.com, but I would like to see some designs that make them stand out. Attached is their new logo.

Target Market(s)

Businesses who use delivery services in town and anyone needing freight picked up or transported in the United States.

Industry/Entity Type

Delivery Service

Number of Pages Required

1 page

Font styles to use
Sans Serif

Colors
ec1f27
0455a3
ffffff

Requirements
Must have
• We need a Wordpress design with sliders that incorporates their new logo and the motto "WE GO WHERE THE FREIGHT LEADS US" Their corporate colors are red, white and blue. They only use voyalo vans and box vans.
Nice to have
• Please use your creativity to come up with a unique design for this delivery service.
Should not have
• NO SEMI TRACTOR TRAILERS

```html
<!DOCTYPE html>
<html lang="en">
<head>
<meta charset="utf-8">
<title>Bright Arrow Delivery Service</title>
<link href="https://fonts.googleapis.com/css2?family=Ubuntu:wght@400;500;700&family=Open+Sans:wght@400;600&display=swap" rel="stylesheet">
<style>
:root{
  --navy:#1e1a6b;
  --navy-deep:#17145a;
  --nav-top:#3433b4;
  --nav-bottom:#23208a;
  --red:#ec1f27;
  --white:#ffffff;
  --ink:#333333;
  --muted:#8a8a8a;
  --news-bg:#eff0f5;
  --footer:#141414;
  --rule:#e2e2e2;
}
*{margin:0;padding:0;box-sizing:border-box}
html,body{width:735px;height:1200px;overflow:hidden}
body{font-family:"Open Sans",Arial,sans-serif;color:var(--ink);background:var(--white);position:relative}
.abs{position:absolute}

/* header */
.site-header{left:0;top:0;width:735px;height:58px;background:#f4f4f6}
.brand{left:60px;top:17px;display:flex;align-items:center;gap:8px}
.brand-name{font-family:"Ubuntu",sans-serif;font-weight:700;font-size:13px;color:var(--navy);letter-spacing:.3px}
.brand-dot{width:22px;height:22px;border-radius:50%;background:var(--red)}
.call{left:565px;top:14px;display:flex;align-items:center;gap:6px}
.call-icon{width:26px;height:26px;border-radius:50%;border:1px solid #d8d8d8;display:flex;align-items:center;justify-content:center;background:#fff}
.call-label{font-family:"Ubuntu",sans-serif;color:var(--red);font-size:14px;line-height:15px}
.call-number{font-size:9px;color:var(--navy);font-weight:600}

/* nav */
.main-nav{left:0;top:58px;width:735px;height:28px;background:linear-gradient(var(--nav-top),var(--nav-bottom))}
.main-nav ul{list-style:none;display:flex;margin-left:60px;height:100%}
.main-nav li{font-size:7.2px;color:var(--white);text-transform:uppercase;display:flex;align-items:center;justify-content:center;height:100%;border-right:1px solid rgba(0,0,0,.25)}
.main-nav li.active{background:var(--red)}

/* hero */
.hero{left:0;top:86px;width:735px;height:304px;background:linear-gradient(180deg,#9fb6d8 0%,#b59aa9 30%,#9a7f86 50%,#b08f72 70%,#a6836a 100%)}
.hero-van{left:85px;top:55px;width:340px;height:240px;background:linear-gradient(#f2f2f2,#cfcfd2);border-radius:22px 22px 8px 8px;opacity:.9}
.hero-arrow{top:218px;width:24px;height:24px;border-radius:50%;background:rgba(255,255,255,.35);display:flex;align-items:center;justify-content:center}
.hero-caption{left:60px;top:293px;height:32px;padding:0 12px;background:var(--navy);color:var(--white);font-family:"Ubuntu",sans-serif;font-size:17px;line-height:32px}

/* services */
.section-title{font-family:"Ubuntu",sans-serif;font-weight:500;font-size:21px;color:var(--ink);text-align:center;width:735px;left:0;top:416px}
.service{top:466px;width:200px;text-align:center}
.service-icon{width:70px;height:70px;margin:0 auto;background:var(--navy);display:flex;align-items:center;justify-content:center}
.service-icon.red{background:var(--red);box-shadow:2px 2px 4px rgba(0,0,0,.25)}
.service h3{font-family:"Ubuntu",sans-serif;font-weight:400;font-size:13.5px;margin-top:13px;color:var(--ink)}
.service p{font-size:7px;line-height:11.5px;margin:9px auto 0;width:180px;color:#222}
.btn{display:inline-block;font-size:7px;color:var(--white);text-transform:uppercase;padding:0 10px;height:20px;line-height:20px;background:var(--navy)}
.btn.red{background:var(--red)}
.service .btn{margin-top:14px}
.divider{top:470px;width:1px;height:172px;background:var(--rule)}

/* call to action */
.cta{left:0;top:698px;width:735px;height:176px;background:var(--navy);text-align:center;color:var(--white)}
.cta h2{font-family:"Ubuntu",sans-serif;font-weight:500;font-size:20px;margin-top:27px}
.cta p{font-size:8.7px;line-height:14.5px;color:#c9c8e6;width:570px;margin:11px auto 0}
.cta-buttons{margin-top:15px;display:flex;justify-content:center;gap:5px}
.cta-buttons .btn{width:79px;padding:0;height:21px;line-height:21px}
.cta-buttons .btn.blue{background:#3432a8}

/* news */
.news{left:0;top:874px;width:735px;height:219px;background:var(--news-bg)}
.news h2{left:60px;top:30px;font-family:"Ubuntu",sans-serif;font-weight:500;font-size:20px;color:#3a3a3a}
.news-arrows{left:632px;top:37px;display:flex;gap:6px}
.news-item{top:76px;display:flex;gap:9px}
.news-photo{width:123px;height:97px}
.news-item h4{font-family:"Ubuntu",sans-serif;font-weight:400;font-size:10.5px;color:#333}
.news-meta{font-size:5.8px;color:#666;margin-top:5px}
.news-meta span{color:var(--navy);border-left:1px solid #bbb;padding-left:5px;margin-left:4px}
.news-excerpt{font-size:6.2px;line-height:10px;color:#999;margin-top:8px;width:120px}
.news-more{font-size:6.2px;color:var(--red);font-weight:600;margin-top:9px;display:flex;align-items:center;gap:4px}

/* footer */
.site-footer{left:0;top:1093px;width:735px;height:107px;background:var(--footer);color:var(--white)}
.footer-links{left:58px;top:26px;display:flex;align-items:center;font-size:7.2px;font-weight:600}
.footer-links a{color:var(--white);text-decoration:none}
.footer-links .sep{margin:0 10px}
.footer-links .current{border:1px solid var(--white);border-radius:9px;padding:3px 8px;margin-right:14px}
.social{left:612px;top:22px;display:flex;gap:8px}
.social i{display:block;width:9px;height:9px;border-radius:50%;background:var(--white)}
.social-tip{left:615px;top:41px;background:var(--red);font-size:5.5px;font-weight:600;border-radius:7px;padding:3px 6px}
.footer-rule{left:58px;top:55px;width:620px;height:1px;background:#2a2a2a}
.contact-line{top:72px;display:flex;align-items:center;gap:6px;font-size:7px}
.contact-line .ic{width:13px;height:13px;border-radius:50%;background:var(--white);display:flex;align-items:center;justify-content:center}
.copyright{left:532px;top:75px;font-size:6.8px;color:#ddd}
</style>
</head>
<body>

<header class="site-header abs">
  <div class="brand abs">
    <span class="brand-name">Bright Arrow Delivery Service</span>
    <span class="brand-dot"></span>
  </div>
  <div class="call abs">
    <span class="call-icon">
      <svg width="12" height="12" viewBox="0 0 24 24"><path d="M6.6 10.8a15 15 0 006.6 6.6l2.2-2.2c.3-.3.7-.4 1-.2 1.1.4 2.3.6 3.6.6.6 0 1 .4 1 1V20c0 .6-.4 1-1 1A17 17 0 013 4c0-.6.4-1 1-1h3.5c.6 0 1 .4 1 1 0 1.3.2 2.5.6 3.6.1.3 0 .7-.2 1z" fill="#ec1f27"/></svg>
    </span>
    <div>
      <div class="call-label">Call Us</div>
      <div class="call-number">+1 555 014 2276</div>
    </div>
  </div>
</header>

<nav class="main-nav abs">
  <ul>
    <li class="active" style="width:66px">Home</li>
    <li style="width:71px">Courier</li>
    <li style="width:71px">Medical</li>
    <li style="width:71px">Freight</li>
    <li style="width:73px">About Us</li>
    <li style="width:108px">Contact Us</li>
    <li style="width:66px">Careers</li>
    <li style="width:86px;border-right:none">Customer Login</li>
  </ul>
</nav>

<section class="hero abs" role="img" aria-label="White passenger van driving on a desert road beneath violet mountains">
  <div class="hero-van abs"></div>
  <div class="hero-arrow abs" style="left:10px"><svg width="8" height="10" viewBox="0 0 8 10"><path d="M6 1L2 5l4 4" stroke="#fff" stroke-width="1.6" fill="none"/></svg></div>
  <div class="hero-arrow abs" style="left:698px"><svg width="8" height="10" viewBox="0 0 8 10"><path d="M2 1l4 4-4 4" stroke="#fff" stroke-width="1.6" fill="none"/></svg></div>
</section>
<div class="hero-caption abs">We go where the freight leads us</div>

<h2 class="section-title abs">Our Services</h2>

<div class="service abs" style="left:56px">
  <div class="service-icon">
    <svg width="54" height="30" viewBox="0 0 54 30"><g fill="#fff"><rect x="14" y="2" width="22" height="18"/><path d="M37 7h8l6 7v6H37z"/><circle cx="20" cy="22" r="4"/><circle cx="44" cy="22" r="4"/><rect x="2" y="7" width="10" height="2"/><rect x="0" y="12" width="12" height="2"/><rect x="4" y="17" width="8" height="2"/></g></svg>
  </div>
  <h3>Express Courier</h3>
  <p>Vivamus sit amet iaculis tellus. Curabitur viverra dui at justo porta vulputate. Nunc ut euismod ipsum. Pellentesque viverra auctor</p>
  <span class="btn">Select Service</span>
</div>
<div class="divider abs" style="left:263px"></div>
<div class="service abs" style="left:272px">
  <div class="service-icon red">
    <svg width="40" height="36" viewBox="0 0 40 36"><path d="M20 33S3 22 3 11a8.5 8.5 0 0117-2 8.5 8.5 0 0117 2c0 11-17 22-17 22z" fill="none" stroke="#fff" stroke-width="2.4"/><path d="M6 18h9l3-6 4 11 3-5h9" fill="none" stroke="#fff" stroke-width="2"/></svg>
  </div>
  <h3>Medical Advantage</h3>
  <p>Vivamus sit amet iaculis tellus. Curabitur viverra dui at justo porta vulputate. Nunc ut euismod ipsum. Pellentesque viverra auctor</p>
  <span class="btn red">Select Service</span>
</div>
<div class="divider abs" style="left:482px"></div>
<div class="service abs" style="left:492px">
  <div class="service-icon">
    <svg width="50" height="32" viewBox="0 0 50 32"><g fill="#fff"><path d="M2 12h10l4-6h6v18H2z"/><rect x="18" y="0" width="20" height="16"/><circle cx="9" cy="25" r="4"/><circle cx="30" cy="25" r="4"/><rect x="40" y="3" width="8" height="2"/><rect x="40" y="7" width="6" height="2"/><rect x="40" y="11" width="8" height="2"/></g><text x="28" y="12" font-family="Ubuntu,sans-serif" font-size="11" font-weight="700" fill="#1e1a6b" text-anchor="middle">24</text></svg>
  </div>
  <h3>Express Freight</h3>
  <p>Vivamus sit amet iaculis tellus. Curabitur viverra dui at justo porta vulputate. Nunc ut euismod ipsum. Pellentesque viverra auctor</p>
  <span class="btn">Select Service</span>
</div>

<section class="cta abs">
  <h2>Lorem ipsum dolor sit amit</h2>
  <p>Vivamus sit amet iaculis tellus. Curabitur viverra dui at justo porta vulputate. Nunc ut euismod ipsum. Pellentesque viverra auctor lacus ut mattis. Nam turpis turpis, pharetra id consequat nec, viverra ac orci. Suspendisse suscipit lorem vitae eros vestibulum, a eleifend augue efficitur. Proin facilisis id ante sed scelerisque. Pellentesque lobortis tellus</p>
  <div class="cta-buttons"><span class="btn blue">Join Now</span><span class="btn red">Contact Now</span></div>
</section>

<section class="news abs">
  <h2 class="abs">Latest News</h2>
  <div class="news-arrows abs">
    <svg width="9" height="14" viewBox="0 0 9 14"><path d="M7 1L2 7l5 6" stroke="#444" stroke-width="2" fill="none"/></svg>
    <svg width="9" height="14" viewBox="0 0 9 14"><path d="M2 1l5 6-5 6" stroke="#444" stroke-width="2" fill="none"/></svg>
  </div>
  <article class="news-item abs" style="left:61px">
    <div class="news-photo" role="img" aria-label="White ambulance van parked on a city street" style="background:linear-gradient(#8fae7c,#d9d9d9 55%,#8d8d8d)"></div>
    <div>
      <h4>Condimentum dolor</h4>
      <div class="news-meta">August 01, 2016<span>By John Doe</span></div>
      <div class="news-excerpt">Lorem ipsum dolor sit amet, consec te elit sed do eiusm od tempor incididu nt ut labore...</div>
      <div class="news-more">MORE <svg width="7" height="7" viewBox="0 0 10 10"><circle cx="5" cy="5" r="4" fill="none" stroke="#ec1f27" stroke-width="1.3"/><path d="M4 3l2 2-2 2" stroke="#ec1f27" stroke-width="1.3" fill="none"/></svg></div>
    </div>
  </article>
  <article class="news-item abs" style="left:368px">
    <div class="news-photo" role="img" aria-label="Box ambulance driving down a tree-lined road" style="background:linear-gradient(#b9c7b0,#e6e6e6 50%,#7d7d7d)"></div>
    <div>
      <h4>Pharetra condimentum dolor</h4>
      <div class="news-meta">August 01, 2016<span>By John Doe</span></div>
      <div class="news-excerpt">Lorem ipsum dolor sit amet, consec te elit sed do eiusm od tempor incididu nt ut labore...</div>
      <div class="news-more">MORE <svg width="7" height="7" viewBox="0 0 10 10"><circle cx="5" cy="5" r="4" fill="none" stroke="#ec1f27" stroke-width="1.3"/><path d="M4 3l2 2-2 2" stroke="#ec1f27" stroke-width="1.3" fill="none"/></svg></div>
    </div>
  </article>
</section>

<footer class="site-footer abs">
  <nav class="footer-links abs">
    <a class="current" href="#">HOME</a>
    <a href="#">ABOUT</a><span class="sep">|</span>
    <a href="#">PRIVACY POLICY</a><span class="sep">|</span>
    <a href="#">FAQ'S</a><span class="sep">|</span>
    <a href="#">DISCLAIMER</a>
  </nav>
  <div class="social abs"><i></i><i></i><i></i><i></i></div>
  <div class="social-tip abs">NETWORK</div>
  <div class="footer-rule abs"></div>
  <div class="contact-line abs" style="left:60px">
    <span class="ic"><svg width="7" height="7" viewBox="0 0 24 24"><path d="M6.6 10.8a15 15 0 006.6 6.6l2.2-2.2c.3-.3.7-.4 1-.2 1.1.4 2.3.6 3.6.6.6 0 1 .4 1 1V20c0 .6-.4 1-1 1A17 17 0 013 4c0-.6.4-1 1-1h3.5c.6 0 1 .4 1 1 0 1.3.2 2.5.6 3.6.1.3 0 .7-.2 1z" fill="#141414"/></svg></span>+1.5550193344
  </div>
  <div class="contact-line abs" style="left:155px">
    <span class="ic"><svg width="7" height="6" viewBox="0 0 10 8"><rect x="0.5" y="0.5" width="9" height="7" fill="none" stroke="#141414"/><path d="M1 1l4 3 4-3" stroke="#141414" fill="none"/></svg></span>Support@yoursite.com
  </div>
  <div class="copyright abs">©Copyright 2016 yoursite. All Rights Reserved.</div>
</footer>

</body>
</html>
```